Young and modern Electrical company working in the commercial arena.

Wanting a business card design thats modern and will last. Maybe Minimalist? Happy to look at changing my logo

Target Market(s)

Builders, Project Managers

Industry/Entity Type

Electrical

Contact Information for Business Card

Name
Address
Phone number
Job title

Logo Text

our name or just the logo i'm open to ideas

Font styles to use
Sans Serif

Requirements
Nice to have
• would like to keep the purple in our current logo. it's kinda unique to our market
Should not have
• Don't want it to be to busy. simple is best i think

```html
<!DOCTYPE html>
<html lang="en">
<head>
<meta charset="utf-8">
<title>Voltline Electrical — Business Card</title>
<link href="https://fonts.googleapis.com/css2?family=Open+Sans:wght@400;600&display=swap" rel="stylesheet">
<style>
  :root {
    --bg: #2a2b2e;
    --card-white: #ffffff;
    --brand-purple: #6a45a8;
    --brand-purple-deep: #5d3b98;
    --text-light: #ffffff;
    --wordmark: #6a45a8;
  }
  * { box-sizing: border-box; margin: 0; padding: 0; }
  html, body {
    width: 1200px; height: 900px; overflow: hidden;
    background: var(--bg);
    font-family: "Open Sans", sans-serif;
  }
  .canvas {
    width: 1200px; height: 900px;
    display: flex; flex-direction: column;
    align-items: center; justify-content: center; gap: 60px;
  }
  .card {
    position: relative;
    width: 620px; height: 354px;
    background: var(--card-white);
    clip-path: polygon(0 0, 100% 0, 100% 100%, 36% 100%, 33% 90%, 0 90%);
    overflow: hidden;
  }
  .wordmark {
    position: absolute; left: 50%; transform: translateX(-50%);
    display: flex; align-items: center; gap: 10px;
    color: var(--wordmark);
    font-weight: 600; font-size: 26px; letter-spacing: 1px;
    white-space: nowrap;
  }
  .wordmark .mark {
    width: 14px; height: 14px; background: var(--wordmark); display: block;
  }
  /* front */
  .card--front .wordmark { top: 150px; }
  .card--front .edge-band {
    position: absolute; left: 0; bottom: 0;
    width: 100%; height: 46px;
    background: var(--brand-purple);
  }
  /* back */
  .card--back .wordmark { top: 58px; font-size: 20px; }
  .card--back .info-band {
    position: absolute; left: 0; bottom: 0;
    width: 100%; height: 58%;
    background: linear-gradient(180deg, var(--brand-purple), var(--brand-purple-deep));
    color: var(--text-light);
    display: flex; align-items: center;
    padding: 0 40px 30px 50px;
  }
  .identity { width: 200px; text-align: right; padding-right: 22px; }
  .identity .person-name { font-weight: 600; font-size: 22px; letter-spacing: 0.5px; }
  .identity .job-title { font-size: 13px; letter-spacing: 1px; margin-top: 2px; }
  .divider { width: 2px; height: 96px; background: var(--text-light); }
  .contacts { list-style: none; padding-left: 20px; }
  .contacts li {
    display: flex; align-items: center; gap: 10px;
    font-size: 14px; margin: 6px 0;
  }
  .contacts .icon {
    width: 24px; height: 24px; border-radius: 50%;
    background: var(--text-light);
    display: flex; align-items: center; justify-content: center;
  }
</style>
</head>
<body>
<main class="canvas">
  <section class="card card--front" aria-label="Card front">
    <div class="wordmark"><span class="mark"></span>voltline electrical</div>
    <div class="edge-band"></div>
  </section>

  <section class="card card--back" aria-label="Card back">
    <div class="wordmark"><span class="mark"></span>voltline electrical</div>
    <div class="info-band">
      <div class="identity">
        <p class="person-name">MAREK DOYLE</p>
        <p class="job-title">DOCTOR</p>
      </div>
      <div class="divider"></div>
      <ul class="contacts">
        <li>
          <span class="icon"><svg width="14" height="14" viewBox="0 0 24 24"><path fill="#6a45a8" d="M6.6 10.8a15 15 0 0 0 6.6 6.6l2.2-2.2c.3-.3.7-.4 1-.2 1.1.4 2.3.6 3.6.6.6 0 1 .4 1 1V20c0 .6-.4 1-1 1A17 17 0 0 1 3 4c0-.6.4-1 1-1h3.5c.6 0 1 .4 1 1 0 1.3.2 2.5.6 3.6.1.3 0 .7-.2 1z"/></svg></span>
          03 5550 4127
        </li>
        <li>
          <span class="icon"><svg width="14" height="14" viewBox="0 0 24 24"><rect x="3" y="6" width="18" height="12" fill="none" stroke="#6a45a8" stroke-width="2"/><path d="M3 6l9 7 9-7" fill="none" stroke="#6a45a8" stroke-width="2"/></svg></span>
          hello@voltlinepower.com.au
        </li>
        <li>
          <span class="icon"><svg width="14" height="14" viewBox="0 0 24 24" fill="none" stroke="#6a45a8" stroke-width="2"><circle cx="12" cy="12" r="9"/><path d="M3 12h18M12 3c3 3 3 15 0 18M12 3c-3 3-3 15 0 18"/></svg></span>
          www.voltlinepower.com.au
        </li>
      </ul>
    </div>
  </section>
</main>
</body>
</html>
```